Etikett für Honigunternehmen gesucht
Zielgruppe
Wir produzieren Honig, möchten aber in naher Zukunft auch andere Honigprodukte produzieren (Cremen, Wein, Likör......). Unsere Zielgruppe sind alle.
Aufgabenstellung
Wir wünschen uns Schlichtheit und Einfachheit. Wichtig ist uns auch, dass das Design modern wirkt. Es soll kein typisches Honigetikett mit 'Wiesen und Bienen' werden. Das Glas wird auch schlicht und modern werden. Es wird nur 250-g- und 500-g-Gläser geben. Die Gewichtsangabe muss sichtbar und mind. 4 mm groß sein. Name, Anschrift und Telefonnummer können auch am Deckel oder ganz klein und leserlich am unteren Etikettenrand stehen. Dabei ist zu beachten, dass der kleinste Buchstabe min. 1,2 mm groß ist.
Etiketten-Design für Honigglas Etiketten-Design für Honigglas"
Format: Etikett für 250-gr.-Honigglas (TO ∅ 63 mm). Standardmaßgrösse 165 × 40 mm Design: schlicht, hochwertig, modern, edel/royal, unkonventionelles Design (weg von Bienen, Waben, Landschaften usw.), dunkle Farbtöne in Kontrast zu heller Schrift, die beiden Textbausteine 'Los Nr. ' sowi..
Attraktives Etiketten-Design für Honig Attraktives Etiketten-Design für Honig"
Wir verkaufen zur Zeit vor allem Waldhonig, streben aber auch einen Blütenhonig an. Das Etikett soll daher entweder den Wald wiederspiegeln oder aber neutral sein, so dass der Schriftzug Waldhonig oder Blütenhonig jeweils eingesetzt werden kann. Wichtig ist mir der Ortszusatz 'aus dem Glottertal..
Etiketten-Design für Produkte eines Familienbetriebs mit Imkerei und Hühnerhaltung Etiketten-Design für Produkte eines Familienbetriebs mit Imkerei und Hühnerhaltung"
1. Zentrale, auf allen Etiketten wiederkehrende Elemente: - Unser Riegelhaus (stilisiert) (Bild beiliegend) - Das Wort 'Marlock' (Anmerkung: ohne Anführungszeichen) - die zentralen Elemente sollen die Produkte nicht überragen. 2. Dezente Adresse: - Familie Obrecht, Talbrunn, CH-9388 Forlenz 3...
Etiketten-Design für Kurkuma-Honig Etiketten-Design für Kurkuma-Honig"
Etikett für 500g // Stanze eckig (210x35mm), Druckdatei entsprechend Vorgaben https://etikettwerk-muster.de/faq/ Vorgaben für das Grünquell Logo im Anhang Vorgaben für EG Öko Logo : https://example-oekoamt.eu/landbau/bio/download/logo_de Pflichtangaben auf dem Etikett: Gewicht, Adresse siehe Beispiel..
Etiketten-Design für Blütenhonig und Waldhonig gesucht Etiketten-Design für Blütenhonig und Waldhonig gesucht"
Zwei verschiedene Etiketten-Desings 1 x Blütenhonig sowie 1 x Waldhonig für unterschiedliche Honigglasgrößen (500 g und 250 g) Die Maße für die Etiketten wären: Für 500-Gramm-Glas 210 mm x 45 mm für's 250-Gramm-Glas 180 mm x 38 mm. Wir sind auch offen für neue Vorschläge bezüglich ..

```html
<!DOCTYPE html>
<html lang="de">
<head>
<meta charset="utf-8">
<title>Anton Honig – Etikett Blütenhonig</title>
<link rel="stylesheet" href="https://fonts.googleapis.com/css2?family=Didact+Gothic&display=swap">
<style>
  :root {
    --bg-top: #fde9bf;
    --bg-bottom: #fef4df;
    --label-white: #ffffff;
    --honey-orange: #f2a516;
    --lavender: #8578bd;
    --band-text: #ffffff;
  }
  * { margin: 0; padding: 0; box-sizing: border-box; }
  html, body {
    width: 1200px;
    height: 849px;
    overflow: hidden;
  }
  body {
    background: linear-gradient(180deg, var(--bg-top) 0%, var(--bg-bottom) 100%);
    font-family: "Didact Gothic", sans-serif;
    position: relative;
  }
  .label {
    position: absolute;
    left: 40px;
    top: 168px;
    width: 1120px;
    height: 512px;
    background: var(--label-white);
    box-shadow: 0 6px 24px rgba(180, 130, 40, 0.12);
  }
  .brand-name {
    position: absolute;
    left: 150px;
    top: 50px;
    color: var(--honey-orange);
    font-size: 118px;
    line-height: 1.05;
    letter-spacing: 2px;
  }
  .brand-name .line-two { display: block; padding-left: 90px; }
  .brand-dot {
    position: absolute;
    left: 690px;
    top: 205px;
    width: 70px;
    height: 70px;
    border-radius: 50%;
    background: var(--honey-orange);
  }
  .producer-info {
    position: absolute;
    left: 148px;
    top: 444px;
    width: 692px;
    color: var(--honey-orange);
    font-size: 21px;
    line-height: 29px;
  }
  .producer-info p { display: flex; justify-content: space-between; white-space: nowrap; }
  .variety-band {
    position: absolute;
    left: 896px;
    top: 0;
    width: 137px;
    height: 100%;
    background: var(--lavender);
    color: var(--band-text);
  }
  .variety-name {
    position: absolute;
    right: 12px;
    top: 28px;
    writing-mode: vertical-rl;
    font-size: 62px;
    line-height: 1;
    letter-spacing: 1px;
  }
  .net-weight {
    position: absolute;
    left: 18px;
    top: 190px;
    writing-mode: vertical-rl;
    font-size: 36px;
    line-height: 1;
  }
</style>
</head>
<body>
  <main class="label">
    <h1 class="brand-name">Anton<span class="line-two">Honig</span></h1>
    <span class="brand-dot" aria-hidden="true"></span>

    <div class="producer-info">
      <p><span>Anton Brenner</span><span>|</span><span>Am Lindenhang 14</span><span>|</span><span>4263 Talbach</span></p>
      <p><span>Herkunftsland</span><span>Österreich</span><span>|</span><span>Tel:</span><span>+436641205874</span></p>
    </div>

    <aside class="variety-band">
      <span class="variety-name">Blütenhonig</span>
      <span class="net-weight">500g</span>
    </aside>
  </main>
</body>
</html>
```